Norvane Builders Business Card

Modern and Professional Business Card for a Med size construction/development company.

See the samples below for the design I like … but I need ideas for incorporating the red company logo while still keeping the clean look of the card samples that are attached.

Logo and tag line on the back … info on the front.

Tagline: Quality Starts from the Ground Up

Target Market(s)

Med-Large General Contractors

Contact Information for Business Card

Norvane Builders Limited
42 Brenton Street
Elk Harbour, NL
B3K 7T2

t: 709-555-0147
f: 709-555-0192
w: www.norvanebuilders-example.com

Font styles to use
Sans Serif

Colors
fbee3e

Requirements
Must have
• I like the black and yellow designs of the attached samples …. but I'm not sure how to incorporate the red Norvane Builders logo into that design??
Nice to have
• Construction safety strips

```html
<!DOCTYPE html>
<html lang="en">
<head>
<meta charset="utf-8">
<title>Norvane Builders Business Card</title>
<link rel="stylesheet" href="https://fonts.googleapis.com/css2?family=Open+Sans:wght@400;600&display=swap">
<style>
  :root {
    --safety-yellow: #e2c309;
    --ink: #1e1e1e;
    --backdrop: #d9d6d0;
  }
  * { box-sizing: border-box; margin: 0; padding: 0; }
  html, body {
    width: 1200px; height: 900px; overflow: hidden;
    background: var(--backdrop);
    font-family: "Open Sans", Arial, sans-serif;
  }
  .sheet {
    width: 1200px; height: 900px;
    display: flex; flex-direction: column; align-items: center; justify-content: center;
    gap: 40px;
  }
  .card {
    position: relative;
    width: 700px; height: 400px;
    overflow: hidden;
    box-shadow: 0 6px 18px rgba(0,0,0,.18);
  }
  .hazard-band {
    position: absolute; left: 0; right: 0; height: 30px;
  }
  .hazard-band--top { top: 18px; }
  .hazard-band--bottom { bottom: 18px; }

  /* back side */
  .card--back { background: var(--safety-yellow); }
  .card--back .hazard-band {
    background: repeating-linear-gradient(-55deg, var(--ink) 0 12px, var(--safety-yellow) 12px 30px);
  }
  .brand-plate {
    position: absolute; left: 50%; top: 118px; transform: translateX(-50%);
    width: 380px; height: 120px;
    background: var(--ink); border-radius: 22px;
    display: flex; align-items: center; justify-content: center; gap: 16px;
  }
  .brand-plate__dot {
    width: 18px; height: 18px; border-radius: 50%; background: var(--safety-yellow);
  }
  .brand-plate__name {
    color: var(--safety-yellow); font-weight: 600; font-size: 26px;
    letter-spacing: 1.5px; text-transform: uppercase; line-height: 1.2;
  }
  .tagline {
    position: absolute; left: 0; right: 0; top: 262px;
    text-align: center; color: var(--ink);
    font-size: 17px; letter-spacing: 2px; text-transform: uppercase;
  }

  /* front side */
  .card--front { background: var(--ink); }
  .card--front .hazard-band {
    background: repeating-linear-gradient(-55deg, var(--safety-yellow) 0 14px, var(--ink) 14px 34px);
  }
  .person {
    position: absolute; left: 42px; top: 158px; width: 320px;
    color: var(--safety-yellow);
  }
  .person__name {
    font-size: 42px; font-weight: 400; letter-spacing: 0.5px; line-height: 1;
    text-transform: uppercase; white-space: nowrap;
  }
  .person__role {
    margin-top: 8px; margin-left: 44px;
    font-size: 19px; letter-spacing: 1px; text-transform: uppercase;
    white-space: nowrap;
  }
  .divider {
    position: absolute; left: 382px; top: 110px; width: 3px; height: 180px;
    background: var(--safety-yellow);
  }
  .contact-list {
    position: absolute; left: 402px; top: 120px; width: 285px; list-style: none;
    color: var(--safety-yellow); font-size: 14px; line-height: 1.3;
  }
  .contact-list li {
    display: flex; align-items: flex-start; gap: 12px; margin-bottom: 16px;
  }
  .contact-list span { white-space: nowrap; }
  .contact-list svg { width: 20px; height: 20px; flex: none; fill: var(--safety-yellow); }
</style>
</head>
<body>
<main class="sheet">

  <section class="card card--back" aria-label="Card back">
    <div class="hazard-band hazard-band--top"></div>
    <div class="brand-plate">
      <span class="brand-plate__dot"></span>
      <span class="brand-plate__name">Norvane Builders<br>Limited</span>
    </div>
    <p class="tagline">Quality Starts from the Ground Up</p>
    <div class="hazard-band hazard-band--bottom"></div>
  </section>

  <section class="card card--front" aria-label="Card front">
    <div class="hazard-band hazard-band--top"></div>
    <div class="person">
      <h1 class="person__name">Daniel Marsh</h1>
      <p class="person__role">Civil Engineer</p>
    </div>
    <div class="divider"></div>
    <ul class="contact-list">
      <li>
        <svg viewBox="0 0 24 24" aria-hidden="true"><path d="M12 2a7 7 0 0 0-7 7c0 5 7 13 7 13s7-8 7-13a7 7 0 0 0-7-7zm0 9.5A2.5 2.5 0 1 1 12 6.5a2.5 2.5 0 0 1 0 5z"/></svg>
        <span>42 Brenton Street Elk Harbour,<br>NL B3K 7T2</span>
      </li>
      <li>
        <svg viewBox="0 0 24 24" aria-hidden="true"><path d="M6.6 10.8a15 15 0 0 0 6.6 6.6l2.2-2.2c.3-.3.7-.4 1-.2 1.1.4 2.3.6 3.6.6.6 0 1 .4 1 1V20c0 .6-.4 1-1 1A17 17 0 0 1 3 4c0-.6.4-1 1-1h3.5c.6 0 1 .4 1 1 0 1.3.2 2.5.6 3.6.1.3 0 .7-.2 1z"/></svg>
        <span>709-555-0147</span>
      </li>
      <li>
        <svg viewBox="0 0 24 24" aria-hidden="true"><rect x="1" y="6" width="11" height="12" rx="1"/><rect x="13" y="4" width="5" height="16" rx="1"/><rect x="20" y="4" width="3" height="16" rx="1"/></svg>
        <span>709-555-0192</span>
      </li>
      <li>
        <svg viewBox="0 0 24 24" aria-hidden="true"><path d="M12 2a10 10 0 1 0 0 20 10 10 0 0 0 0-20zm0 2c.9 1.2 1.7 2.8 2.1 5H9.9c.4-2.2 1.2-3.8 2.1-5zM4.3 9h3.6a17 17 0 0 0 0 6H4.3a8 8 0 0 1 0-6zm5.6 0h4.2a15 15 0 0 1 0 6H9.9a15 15 0 0 1 0-6zm6.2 0h3.6a8 8 0 0 1 0 6h-3.6a17 17 0 0 0 0-6zM12 20c-.9-1.2-1.7-2.8-2.1-5h4.2c-.4 2.2-1.200 3.8-2.1 5z"/></svg>
        <span>www.norvanebuilders-example.com</span>
      </li>
    </ul>
    <div class="hazard-band hazard-band--bottom"></div>
  </section>

</main>
</body>
</html>
```